Gestatlung flyer (2 pages) format selectable, based accompanying templates (logo, text) Projektflyer "intercultural cooking class with asylum seekers' data Friday evenings 17. 03 / 24.03 / 31.03 / 07.04 / Time: 18:30 Location: KB Merlital St. Gallen Title: Intercultural cooking class with asylum seekers text: cooking course is run by asylum seekers. Cooking together, outlandish specialties, exciting conversations Registration: until 24h before the event costs: Expenses participation at its discretion Logos: Quarzo Linde, Stifung Velmora. The logos should be listed as the sender and do not dominate the flyer. --------- Just be creative, everything is permitted and desired. The goal is that we make as many people as possible aware of this flyer. The flyers are distributed and the target audience is young adults. Dr Flyer should be correspondingly Modern, Emotianal and sales driven (screaming). Strong Typo, clearly legible and the content clearly structured. The shape of the flyer is free! In total we leave you as much creative freedom as possible. I am looking forward to the many great suggestions and am very excited about the results.

Target Market(s)

Young adults

Font styles to use
Serif
Sans Serif
Script

Requirements
Must have
• Textunterstüzung by appropriate images. Friendly design, bright colors. Very easy to read, weighted Title entsrprechend.
Nice to have
• Emotional Cook image or illustration
Should not have
• No picture with white and dark-skinned people.

```html
<!DOCTYPE html>
<html lang="de">
<head>
<meta charset="utf-8">
<title>Interkultureller Kochkurs – Flyer</title>
<link rel="stylesheet" href="https://fonts.googleapis.com/css2?family=Anton&family=Oswald:wght@300;500&family=Lato:wght@400;700&display=swap">
<style>
  :root {
    --magenta: #e01fd8;
    --magenta-deep: #c512c4;
    --lime: #8ef01f;
    --lime-deep: #6fd40c;
    --cyan: #34f0ee;
    --ink: #111111;
    --night: #1c1c1e;
    --paper: #f6f6f6;
    --stage: #c9cccf;
  }
  * { margin: 0; padding: 0; box-sizing: border-box; }
  html, body { width: 1200px; height: 1178px; overflow: hidden; background: var(--stage); }
  .flyer {
    position: absolute; left: 201px; top: 24px;
    width: 962px; height: 1360px;
    transform: scale(0.83); transform-origin: 0 0;
    background: linear-gradient(180deg, #ffffff 0%, var(--paper) 100%);
    overflow: hidden;
    box-shadow: 0 8px 30px rgba(0,0,0,.35);
  }
  .flyer-art { position: absolute; inset: 0; width: 962px; height: 1360px; }
  .brand {
    position: absolute; left: 560px; top: 56px;
    display: flex; align-items: center; gap: 14px;
    font: 400 50px/1 "Lato", sans-serif; color: var(--ink);
  }
  .brand-mark { width: 22px; height: 22px; background: var(--ink); }
  .info { position: absolute; left: 640px; width: 322px; text-align: center; }
  .info-label { font: 400 48px/1 "Anton", sans-serif; color: var(--cyan); }
  .time-label { top: 306px; left: 660px; width: 260px; }
  .time-value {
    position: absolute; left: 735px; top: 374px; width: 170px; height: 48px;
    background: var(--lime); color: var(--ink);
    font: 400 40px/48px "Anton", sans-serif; text-align: center;
  }
  .dates-label { top: 454px; left: 660px; width: 260px; }
  .dates-weekday {
    position: absolute; left: 660px; top: 505px; width: 300px; text-align: center;
    font: 500 36px/1 "Oswald", sans-serif; color: #fff; letter-spacing: -0.5px;
  }
  .dates-band {
    position: absolute; left: 647px; top: 554px; width: 315px; height: 43px;
    background: var(--lime);
    font: 400 25px/43px "Anton", sans-serif; color: var(--ink); padding-left: 4px;
  }
  .place-label { top: 632px; left: 660px; width: 300px; }
  .place-band {
    position: absolute; left: 567px; top: 694px; width: 395px; height: 44px;
    background: var(--lime);
    font: 400 33px/44px "Anton", sans-serif; color: var(--ink); padding-left: 58px;
  }
  .sender {
    position: absolute; left: 47px; top: 670px;
    display: flex; align-items: center; gap: 12px;
    font: 700 26px/1 "Lato", sans-serif; color: #8a8a8a;
  }
  .sender-mark { width: 22px; height: 22px; background: var(--magenta); transform: rotate(45deg); }
  .headline { position: absolute; left: 42px; top: 744px; font-family: "Anton", sans-serif; }
  .headline-top { display: block; font-size: 50px; line-height: 58px; color: var(--ink); }
  .headline-accent { display: block; font-size: 64px; line-height: 70px; color: var(--lime-deep); }
  .lead {
    position: absolute; left: 55px; top: 890px;
    font: 700 22px/1.2 "Lato", sans-serif; color: #333;
  }
  .features {
    position: absolute; left: 40px; top: 926px; display: flex; gap: 14px;
    list-style: none; font: 700 16px/1.2 "Lato", sans-serif; color: #444;
  }
  .features li::before { content: "•"; color: var(--magenta); margin-right: 7px; }
  .cost {
    position: absolute; left: -4px; top: 972px; width: 591px; height: 86px;
    border: 3px solid var(--magenta); border-left: none; border-radius: 0 24px 24px 0;
    background: linear-gradient(180deg, #fbfbfb, #ececec);
    box-shadow: 0 12px 18px -10px rgba(0,0,0,.25);
    font: 300 35px/80px "Oswald", sans-serif; color: var(--ink); padding-left: 44px; letter-spacing: -0.5px;
  }
  .deadline {
    position: absolute; left: 96px; top: 1124px; width: 214px; height: 228px;
    background: linear-gradient(180deg, #a8ff3a, var(--lime-deep));
    border-radius: 22px; text-align: center;
  }
  .deadline-pre { display: block; margin-top: 30px; font: 500 48px/1 "Oswald", sans-serif; color: var(--ink); }
  .deadline-hours { display: block; font: 400 88px/1 "Anton", sans-serif; color: var(--magenta); margin-top: 4px; }
  .deadline-post { display: block; font: 400 20px/1 "Lato", sans-serif; color: var(--ink); margin-top: 10px; }
  .callout {
    position: absolute; left: 342px; top: 1262px;
    font: 400 45px/1 "Anton", sans-serif; color: var(--cyan); letter-spacing: 0.3px;
  }
</style>
</head>
<body>
<main class="flyer">
  <svg class="flyer-art" viewBox="0 0 962 1360" xmlns="http://www.w3.org/2000/svg">
    <defs>
      <linearGradient id="panelFill" x1="0" y1="0" x2="0" y2="1">
        <stop offset="0" stop-color="#ea3ce3"/>
        <stop offset="1" stop-color="#d014cc"/>
      </linearGradient>
      <linearGradient id="kitchenTone" x1="0" y1="0" x2="1" y2="1">
        <stop offset="0" stop-color="#8a4a36"/>
        <stop offset=".5" stop-color="#c9a48c"/>
        <stop offset="1" stop-color="#b83a2a"/>
      </linearGradient>
      <linearGradient id="homeTone" x1="0" y1="0" x2="1" y2="1">
        <stop offset="0" stop-color="#e8e2dc"/>
        <stop offset="1" stop-color="#9a8f88"/>
      </linearGradient>
      <linearGradient id="chefTone" x1="0" y1="0" x2="0" y2="1">
        <stop offset="0" stop-color="#fafafa"/>
        <stop offset=".35" stop-color="#e6c3a8"/>
        <stop offset="1" stop-color="#f2f2f2"/>
      </linearGradient>
    </defs>

    <!-- magenta information panel -->
    <path d="M962 70 C 860 150, 760 200, 700 250 C 600 340, 520 520, 540 640 C 560 760, 640 900, 760 1360 L 962 1360 Z" fill="#8ef01f"/>
    <path d="M962 92 C 862 170, 770 218, 716 264 C 620 350, 540 520, 558 640 C 578 760, 660 900, 780 1360 L 962 1360 Z" fill="url(#panelFill)"/>

    <!-- main photo circle with rings -->
    <circle cx="250" cy="270" r="352" fill="#8ef01f"/>
    <circle cx="250" cy="262" r="338" fill="#e01fd8"/>
    <circle cx="250" cy="262" r="318" fill="#ffffff"/>
    <circle cx="250" cy="258" r="312" fill="#34f0ee"/>
    <circle cx="250" cy="256" r="304" fill="url(#kitchenTone)" role="img" aria-label="Foto: Gruppe junger Leute kocht gemeinsam mit einem Koch in einer Küche"/>

    <!-- small photo circles -->
    <circle cx="598" cy="272" r="118" fill="#8ef01f"/>
    <circle cx="598" cy="272" r="108" fill="#e01fd8"/>
    <circle cx="598" cy="272" r="102" fill="url(#homeTone)" role="img" aria-label="Foto: Frau zieht eine Pizza aus dem Ofen"/>
    <circle cx="542" cy="504" r="122" fill="#8ef01f"/>
    <circle cx="542" cy="504" r="112" fill="#e01fd8"/>
    <circle cx="542" cy="504" r="106" fill="url(#homeTone)" role="img" aria-label="Foto: Mutter und Tochter spielen mit Paprikaringen in der Küche"/>

    <!-- bottom stripes and dark band -->
    <path d="M0 1210 Q 420 1110 962 1245 L 962 1262 Q 420 1130 0 1226 Z" fill="#e01fd8"/>
    <path d="M0 1224 Q 420 1128 962 1262 L 962 1272 Q 420 1142 0 1236 Z" fill="#34f0ee"/>
    <path d="M0 1236 Q 420 1150 962 1280 L 962 1360 L 0 1360 Z" fill="#1c1c1e"/>

    <!-- chef portrait area -->
    <path d="M700 820 C 760 780, 860 790, 962 830 L 962 1292 C 860 1260, 740 1240, 650 1225 C 660 1080, 660 930, 700 820 Z" fill="url(#chefTone)" role="img" aria-label="Foto: lächelnde Köchin mit Kochmütze zeigt das OK-Zeichen"/>

    <!-- ribbon fold of the deadline badge -->
    <path d="M96 1140 Q 40 1150 44 1220 L 44 1320 Q 60 1270 96 1268 Z" fill="#5fb80a"/>
  </svg>

  <div class="brand"><span class="brand-mark"></span>Quarzo Linde</div>

  <div class="info info-label time-label">Zeit:</div>
  <div class="time-value">18.30h</div>
  <div class="info info-label dates-label">Daten:</div>
  <div class="dates-weekday">Freitag Abende</div>
  <div class="dates-band">17. 03 / 24.03 / 31.03 / 07.04/</div>
  <div class="info info-label place-label">Ort:</div>
  <div class="place-band">KB Merlital St.Gallen</div>

  <div class="sender"><span class="sender-mark"></span>Stifung Velmora</div>

  <h1 class="headline">
    <span class="headline-top">interkultureller Kochkurs</span>
    <span class="headline-accent">mit Asylsuchenden</span>
  </h1>
  <p class="lead">Kochkurs wird von Asylsuchenden geleitet.</p>
  <ul class="features">
    <li>Gemeinsames Kochen,</li>
    <li>Fremdländische Spezialiäten,</li>
    <li>spannende Gespräche.</li>
  </ul>

  <p class="cost">Unkostenbeteiligung nach eigenem Ermessen</p>

  <div class="deadline">
    <span class="deadline-pre">Bis</span>
    <span class="deadline-hours">24h</span>
    <span class="deadline-post">vor dem Anlass</span>
  </div>

  <p class="callout">CALL US NOW: 123 456 7890</p>
</main>
</body>
</html>
```